Fast growing Tech company needs redesign of Veltrana's end user website!

We need to have our login screen, the dashboard, and the one page of the Veltrana site to be redesigned for the end-users. Veltrana is a document hosting service for title companies and real estate law firms. This allows the buyers and sellers to view their closing documents after closing along with many other features that help them out during the closing of their property. More information about what we do can be found on our test site https://qpx.524.sampledraft-host.com/. PLEASE NOTE: THE ABOVE SITE IS NOT THE ONE WE NEED REDONE. The above site is our corporate site that explains our service offering and we thought it would be helpful in providing you a better understanding of our service.
The site that we want to have redesigned is for the end user. THE SITE THAT NEEDS TO BE REDONE ARE THE SCREENSHOTS ATTACHED. We will need the login screen, dashboard, and the one page redesigned.
.
We will just need this in HTML and we will then do the rest for the placeholders for logos, data, mapping etc.
Overall, we want a new, fresh, and modern look for the website and we want the login screen, dashboard and one page website to be consistent in design. Again, these are the three screenshots that are attached.
For the winner, we will most likely need to hire you again for more sites because we have other versions.
Thank you and if any questions, please let us know.
Target Market(s)
This site is for buyer and sellers during the closing process of real estate transaction.

```html
<!DOCTYPE html>
<html lang="en">
<head>
<meta charset="UTF-8">
<title>Veltrana – Login</title>
<link href="https://fonts.googleapis.com/css2?family=Poppins:wght@300;400;500;600&family=Lato:wght@400;700&display=swap" rel="stylesheet">
<style>
  :root{
    --brand:#35a4d8;
    --brand-dark:#2b93c6;
    --ink:#2f3a44;
    --muted:#9aa3ab;
    --line:#c9ced3;
    --page:#f7f8fa;
    --white:#ffffff;
  }
  *{box-sizing:border-box;margin:0;padding:0}
  html,body{width:1200px;height:675px;overflow:hidden;background:var(--page);font-family:"Poppins",sans-serif;color:var(--ink)}
  .site{position:absolute;left:87.5px;top:0;width:1025px;height:675px;background:var(--white)}
  .site-header{position:absolute;left:0;top:0;width:100%;height:83px;border:1px solid var(--brand);border-bottom-width:1.5px;background:var(--white);display:flex;align-items:center;justify-content:center}
  .wordmark{font-family:"Poppins",sans-serif;font-weight:500;font-size:34px;color:var(--brand);letter-spacing:0.5px}
  .hero{position:absolute;left:0;top:83px;width:100%;height:508px;
    background:linear-gradient(100deg,#e9ecef 0%,#dfe3e8 25%,#eef0f2 45%,#c9d3de 70%,#e6dcd6 100%)}
  .login-card{position:absolute;left:330px;top:36px;width:365px;height:437px;background:var(--white)}
  .card-title{position:absolute;top:88px;width:100%;text-align:center;font-weight:600;font-size:14px;letter-spacing:4px;color:var(--brand)}
  .card-tagline{position:absolute;top:107px;width:100%;text-align:center;font-weight:400;font-size:10px;letter-spacing:2px;color:var(--ink)}
  .card-greeting{position:absolute;top:133px;width:100%;text-align:center;font-weight:300;font-size:9px;color:var(--muted)}
  .field{position:absolute;left:91px;width:182px;height:22px;border-bottom:1px solid var(--line);font-family:"Lato",sans-serif;font-size:9px;color:var(--ink);padding:4px 0 0 4px}
  .field.email{top:168px}
  .field.password{top:215px}
  .options{position:absolute;left:91px;top:254px;width:182px;display:flex;justify-content:space-between;align-items:center;font-family:"Lato",sans-serif;font-size:6px;color:var(--ink)}
  .remember{display:flex;align-items:center;gap:6px}
  .checkbox{width:7.5px;height:7.5px;border:1px solid #8a939b;border-radius:2px}
  .actions{position:absolute;left:91px;top:278px;width:182px;display:flex;justify-content:space-between}
  .btn{width:84px;height:22.5px;display:flex;align-items:center;justify-content:center;font-family:"Lato",sans-serif;font-size:7.5px;border-radius:2px}
  .btn-primary{background:var(--brand);color:var(--white);border:1px solid var(--brand-dark)}
  .btn-outline{background:var(--white);color:var(--ink);border:1.5px solid var(--brand)}
  .legal{position:absolute;top:418px;width:100%;text-align:center;font-size:7.5px;color:var(--ink)}
  .site-footer{position:absolute;left:0;top:591px;width:100%;height:84px;background:var(--brand);color:var(--white)}
  .footer-mark{position:absolute;left:11px;top:14px;font-weight:500;font-size:30px;letter-spacing:0.5px}
  .footer-copy{position:absolute;left:48px;top:64px;font-size:8.5px;font-weight:400}
  .footer-nav a{position:absolute;top:26px;font-size:9.5px;color:var(--white);text-decoration:none;font-weight:400}
  .to-top{position:absolute;left:982px;top:14px}
  .social{position:absolute;top:63px;width:8px;height:8px;border-radius:50%;background:var(--white)}
</style>
</head>
<body>
  <div class="site">
    <header class="site-header">
      <span class="wordmark">veltrana</span>
    </header>

    <section class="hero" role="img" aria-label="Softly faded photo of a model house beside papers and a hand signing documents">
      <div class="login-card">
        <div class="card-title">VELTRANA</div>
        <div class="card-tagline">Staying in the Loop</div>
        <div class="card-greeting">Hey there! Please login to your account.</div>
        <div class="field email">Your Email Address</div>
        <div class="field password">Your Password</div>
        <div class="options">
          <span class="remember"><span class="checkbox"></span>Remember me</span>
          <span>Forgot your&nbsp; Password?</span>
        </div>
        <div class="actions">
          <span class="btn btn-primary">Login</span>
          <span class="btn btn-outline">Sign up</span>
        </div>
        <div class="legal">Terms and Conditions |&nbsp; Privacy policy</div>
      </div>
    </section>

    <footer class="site-footer">
      <div class="footer-mark">veltrana</div>
      <div class="footer-copy">VELTRANA® 2021</div>
      <nav class="footer-nav">
        <a style="left:268px">HOME</a>
        <a style="left:365px">ABOUT</a>
        <a style="left:457px">PRE-CLOSE</a>
        <a style="left:551px">POST-CLOSE</a>
        <a style="left:636px">GROWTH</a>
        <a style="left:698px">CONTACT US</a>
      </nav>
      <svg class="to-top" width="12" height="12" viewBox="0 0 12 12" aria-label="Back to top">
        <path d="M6 11V1M1.5 5.5L6 1l4.5 4.5" stroke="#fff" stroke-width="1.4" fill="none"/>
      </svg>
      <span class="social" style="left:934px"></span>
      <span class="social" style="left:961px"></span>
      <span class="social" style="left:987px"></span>
    </footer>
  </div>
</body>
</html>
```